Make it cool to work near where you are...

Calling all creatives - create the ultimate cool card for people who want to cut their commute.

Here at TilloPod we've got what can best be described as an Marlin pass for desks - and we want to brighten up the wallets of our most loyal users.

So, pitch us your ideas and you might see your design on cards being flashed across the country - and we've thrown in a bit of cash too.

Do see our brief card guidelines - with a couple of past examples thrown in.

Industry/Entity Type

Cash

```html
<!DOCTYPE html>
<html lang="en">
<head>
<meta charset="utf-8">
<title>TilloPod Marlin pass card</title>
<link rel="stylesheet" href="https://fonts.googleapis.com/css2?family=Montserrat:wght@700&family=Arimo:wght@400&display=swap">
<style>
  :root {
    --stage: #b9b9bb;
    --card-dark: #2b2a2c;
    --card-dark-soft: #3a383b;
    --pink: #e8197e;
    --white: #ffffff;
    --band-grey: #d3d2d4;
    --ink: #1e1d1f;
  }
  * { box-sizing: border-box; margin: 0; padding: 0; }
  html, body {
    width: 1200px; height: 900px; overflow: hidden;
    background: var(--stage);
  }
  .stage {
    position: relative; width: 1200px; height: 900px;
  }
  .card {
    position: absolute; top: 280px;
    width: 520px; height: 340px;
    border-radius: 26px; overflow: hidden;
    background: var(--card-dark);
  }
  .card--front { left: 50px; }
  .card--back { left: 630px; }

  /* front */
  .front-pattern {
    position: absolute; inset: 0;
    background: linear-gradient(160deg, var(--card-dark-soft) 0%, #4a3840 45%, var(--card-dark) 80%);
  }
  .headline {
    position: absolute; left: 34px; top: 62px;
    font-family: "Montserrat", sans-serif; font-weight: 700;
    font-size: 33px; line-height: 1.02; letter-spacing: -0.5px;
    color: var(--white);
  }
  .headline .accent { color: var(--pink); }
  .front-rule {
    position: absolute; left: 0; right: 0; top: 240px;
    height: 4px; background: var(--pink);
  }
  .brand-tag {
    position: absolute; right: 28px; top: 216px;
    display: flex; align-items: center; gap: 6px;
    padding: 6px 12px;
    background: var(--white); border-radius: 8px;
    font-family: "Montserrat", sans-serif; font-weight: 700;
    font-size: 20px; color: var(--pink);
  }
  .brand-tag .square {
    width: 12px; height: 12px; background: var(--pink);
  }
  .web {
    position: absolute; left: 0; right: 0;
    text-align: center;
    font-family: "Arimo", sans-serif; font-size: 15px;
    color: var(--white);
  }
  .web .accent { color: var(--pink); }
  .card--front .web { top: 284px; }

  /* back */
  .back-pattern {
    position: absolute; left: 0; right: 0; top: 0; height: 168px;
    background: linear-gradient(135deg, var(--pink) 0%, #7a2550 30%, var(--card-dark) 55%, #c2185f 80%, var(--card-dark-soft) 100%);
  }
  .back-strip-line {
    position: absolute; left: 0; right: 120px; top: 196px;
    height: 3px; background: var(--white);
  }
  .card--back .brand-tag { top: 176px; }
  .number-band {
    position: absolute; left: 0; right: 0; top: 214px; height: 38px;
    background: var(--band-grey);
    display: flex; align-items: center; padding-left: 34px;
    font-family: "Arimo", sans-serif; font-size: 21px; letter-spacing: 1px;
    color: var(--ink);
  }
  .back-rule {
    position: absolute; left: 0; right: 0; top: 264px;
    height: 3px; background: var(--white);
  }
  .card--back .web { top: 290px; }
</style>
</head>
<body>
<main class="stage">
  <section class="card card--front" aria-label="Card front">
    <div class="front-pattern" role="img" aria-label="Faint repeating brand-name pattern in dark tones"></div>
    <h1 class="headline">
      <span class="accent">Online accounting<br>for small businesss,</span><br>
      contractors and<br>freelancers.
    </h1>
    <div class="front-rule"></div>
    <div class="brand-tag"><span class="square"></span>TilloPod</div>
    <p class="web">www.<span class="accent">Tillo</span>Pod.com</p>
  </section>

  <section class="card card--back" aria-label="Card back">
    <div class="back-pattern" role="img" aria-label="Repeating brand-name pattern in pink, white and grey"></div>
    <div class="back-strip-line"></div>
    <div class="brand-tag"><span class="square"></span>TilloPod</div>
    <div class="number-band">0020 555 014 862</div>
    <div class="back-rule"></div>
    <p class="web">www.<span class="accent">Tillo</span>Pod.com</p>
  </section>
</main>
</body>
</html>
```